Book Cover design for Tomely and print book.

I’m looking for a unique and fresh approach for this book cover design because the content has a unique and fresh approach. For example I don't want a design that has steps, bulls eyes, targets or trophies. Because it incorporates some of the spiritual elements of goal setting I’d like it to encompass my signature purple colour #330066.

Think about people who want to set unrealistic or aspirational goals that will change the world - rather than people who want to achieve a simple goal.

I want a cover that will work for Tomely and for a print book, and, possibly later, a workbook.

NB My company logo is not intended to go onto the book, it's for your information only. However, an ISBN number will be included.

Target Market(s)

20-60 year old professional men and women who are motivated and want to achieve huge, aspirational goals while enjoying the journey.

Font styles to use
Serif
Sans Serif
Other font styles liked:
• I use Agenda in my manuals, but this isn't essential.

Requirements
Must have
• I prefer rounded shapes rather than sharp angles - but I'm pretty open to new designs. I also prefer font to be set in a combination of upper and lower case letters.
Nice to have
• purple colour #330066 if possible. I don't expect this to be all over the cover. Taking a quick look at my website http://quillfernworks.co.nz might help. Otherwise I'm open to colour, but not a fan of green.
• I like the cleverness and simplicity of Hooked by Wonder, (http://www.bookvarlo-example.com/Hooked-Wonder-Linger-Others-published/dp/Q7R2K9P1ZX/ref=sr_1_4?s=books&ie=UTF8&qid=7302915586&sr=1-4&keywords=Hooked+by+Wonder) In fact all the book covers of Marlo and Teo Brannick's books are impressive.
Should not have
• Bulls eyes, steps, targets or other symbols traditionally associated with goal setting.

```html
<!DOCTYPE html>
<html lang="en">
<head>
<meta charset="utf-8">
<title>Bold Aims: Seven Keys to Unlock Extraordinary Growth – Cover Spread</title>
<link rel="stylesheet" href="https://fonts.googleapis.com/css2?family=Open+Sans:wght@400;700&family=Overpass:wght@600;700;800;900&display=swap">
<style>
  :root {
    --brand-purple: #330066;
    --deep-purple: #3a0f6b;
    --violet: #5b2a9c;
    --magenta: #b0306a;
    --pink: #e39ab8;
    --blush: #f6dbe6;
    --ink: #3c3c3c;
    --muted: #555;
    --paper: #ffffff;
  }
  * { box-sizing: border-box; margin: 0; padding: 0; }
  html, body { width: 1200px; height: 777px; overflow: hidden; background: var(--paper); }
  .spread { position: relative; width: 1200px; height: 777px; overflow: hidden; background: var(--paper); }

  .ink-wash {
    position: absolute; inset: 0;
    background:
      radial-gradient(ellipse 110px 190px at 600px 120px, rgba(58,15,107,.95), rgba(91,42,156,.7) 45%, rgba(176,48,106,.35) 70%, transparent 100%),
      radial-gradient(ellipse 230px 330px at 600px 150px, rgba(227,154,184,.55), rgba(246,219,230,.35) 60%, transparent 100%),
      radial-gradient(ellipse 140px 120px at 30px 777px, rgba(91,42,156,.6), rgba(227,154,184,.3) 60%, transparent 100%),
      radial-gradient(ellipse 150px 130px at 1180px 777px, rgba(91,42,156,.6), rgba(227,154,184,.3) 60%, transparent 100%),
      radial-gradient(ellipse 120px 200px at 1200px 470px, rgba(227,154,184,.35), transparent 100%);
  }
  .spine { position: absolute; left: 600px; top: 0; width: 1px; height: 777px; background: #cfcfcf; }

  .back-copy {
    position: absolute; left: 54px; top: 201px; width: 378px;
    font-family: "Open Sans", sans-serif; font-size: 12.6px; line-height: 20.8px; color: var(--ink);
  }
  .back-copy p { margin-bottom: 8px; }
  .back-copy strong { font-weight: 700; }

  .series-label {
    position: absolute; left: 705px; top: 73px;
    font-family: "Overpass", sans-serif; font-weight: 700; font-size: 21px; line-height: 19px;
    color: var(--brand-purple); letter-spacing: .5px;
  }
  .title-art { position: absolute; left: 0; top: 0; }
  .subtitle {
    position: absolute; left: 814px; top: 649px;
    font-family: "Overpass", sans-serif; font-weight: 600; font-size: 14.6px; line-height: 16px; color: var(--muted);
  }
  .subtitle strong { color: var(--brand-purple); font-weight: 800; }
  .author {
    position: absolute; left: 996px; top: 682px; width: 131px; height: 27px;
    border-radius: 14px; background: var(--brand-purple); color: #fff;
    font-family: "Overpass", sans-serif; font-weight: 700; font-size: 13.5px;
    display: flex; align-items: center; justify-content: center;
  }
</style>
</head>
<body>
<main class="spread">
  <div class="ink-wash" role="img" aria-label="Mirrored watercolour ink bloom in violet, magenta and pink spreading from the top of the spine"></div>
  <div class="spine"></div>

  <section class="back-copy">
    <p>If you’ve ever failed to achieve a goal - (and let’s face it - who hasn’t?) <strong>then this book is for you.</strong></p>
    <p>By applying the 7 keys that make up the <strong>S.U.N.R.I.S.E.</strong> goal setting strategy you’ll learn to cover all the bases that other goal setting models lack. Use the strategy to set completely unrealistic goals; goals that will challenge you to grow and develop while having the most awesome fun on the way to achieving your dreams.</p>
    <p><strong>S.U.N.R.I.S.E.</strong> Goal setting will show you why some goals can feel as if you’re crawling towards them at snails pace, on your hands and knees - over broken glass! You learn how to set goals that, while stretching you, also seem easy and pleasurable. The <strong>S.U.N.R.I.S.E.</strong> strategy incorporates the latest in neuro-scientific research combined with traditional and spiritual wisdom. It’s packed with examples that clarify each key.</p>
    <p><strong>Rowena Calder</strong> is an internationally recognised Writer, Master Trainer and Coach/Mentor. In this book, she’s combined her 20 years experience to show you what works, as well as what definitely doesn’t work to create the future you desire.</p>
  </section>

  <h1 class="series-label">BOLD<br>AIMS:</h1>

  <svg class="title-art" width="1200" height="777" viewBox="0 0 1200 777" aria-label="Seven Keys to unlock Extraordinary Growth">
    <defs>
      <linearGradient id="nebula" x1="0" y1="0" x2="0.6" y2="1">
        <stop offset="0" stop-color="#1e1030"/>
        <stop offset="0.35" stop-color="#5a1f4e"/>
        <stop offset="0.6" stop-color="#3d2a8a"/>
        <stop offset="0.85" stop-color="#c079b0"/>
        <stop offset="1" stop-color="#f0c4dc"/>
      </linearGradient>
    </defs>
    <rect x="706" y="119" width="406" height="433" rx="44" fill="url(#nebula)" role="img" aria-label="Soft starry violet-to-pink sky gradient panel"/>
    <g stroke="#fff" stroke-width="2" opacity=".8">
      <line x1="1040" y1="230" x2="1086" y2="140"/>
      <line x1="1054" y1="230" x2="1096" y2="148"/>
    </g>
    <g font-family="Overpass, sans-serif" font-weight="900" fill="#fff">
      <text x="734" y="448" font-size="92">Seven</text>
      <text x="734" y="528" font-size="92">Keys</text>
    </g>
    <g fill="none" stroke="var(--brand-purple)" stroke-width="2.4">
      <path d="M740 577 H704 L688 592 L704 608 H718"/>
      <path d="M990 577 H1044 L1030 596 L1044 612 H1018"/>
      <path d="M802 552 V692 H996"/>
      <path d="M1127 695 H1148 M1138 687 L1149 695 L1138 703"/>
    </g>
    <g font-family="Overpass, sans-serif" font-weight="700" fill="var(--brand-purple)" text-anchor="middle">
      <text x="866" y="587" font-size="26">to unlock</text>
      <text x="866" y="619" font-size="26">Extraordinary Growth</text>
    </g>
  </svg>

  <p class="subtitle">Using the <strong>S.U.N.R.I.S.E.</strong> strategy<br>to create your future.</p>
  <div class="author">Rowena Calder</div>
</main>
</body>
</html>
```